Emergency Vehicle Installer and Security Firm Needs a Business Card

Our company "Corvalt" need a business card for our Emergency Vehicle Equipment Installation and Infrastructure Security Business. We are contract designers, manufacturers and installers for Emergency Vehicle Fleets. This includes installation of Emergency Lights, Sirens, Vehicle Graphics and Radio Communications. We also supply this products to an international market. We also do consultant, and installation of high level security access, alarm and surveillance equipment for medium to large size businesses.

The design should represent a level of trust in our professionalism and expertise. It should visually display our ongoing relationship with the emergency services, but not overtake our commitment to high level security options.

Target Market(s)

Emergency Services and Businesses requiring high level security

Industry/Entity Type

Business

Contact Information for Business Card

*note complete details will be given to the winning designer for revising. The name "Mark Pell will be used to fill in name".

Mark Pell
Managing Director
Corvalt NZ Limited
Phone: +64 027 604 91352
Email: mark.pell@corvalt-example.co.nz

Requirements
Must have
• Card must be in black. Using our logo on the top as supplied. Designers should try having the reverse side as a blurred image of police lights (red and blue) with our logo in greyscale in the centre (this is not particularly a requirement, but feel free to play around with this option).
Nice to have
• A card design that looks good when spot UV printed. A clean compact and graphic design. A grey scale feel on the front (excluding logo, but you can play around with that idea). Rounded smooth text.
Should not have
• Will update this section as designs come through - feel free to submit what you feel would look good.

```html
<!DOCTYPE html>
<html lang="en">
<head>
<meta charset="utf-8">
<title>Corvalt Business Card</title>
<link href="https://fonts.googleapis.com/css2?family=Open+Sans:wght@400;600;800&display=swap" rel="stylesheet">
<style>
  :root {
    --stage: #2a2a2a;
    --card-black: #050505;
    --card-white: #ffffff;
    --ink: #111111;
    --accent-red: #e52421;
    --muted: #333333;
  }
  * { box-sizing: border-box; margin: 0; padding: 0; }
  html, body {
    width: 1200px; height: 900px; overflow: hidden;
    background: var(--stage);
    font-family: "Open Sans", Arial, sans-serif;
  }
  .stage { position: relative; width: 1200px; height: 900px; }
  .card {
    position: absolute; width: 560px; height: 320px;
    border-radius: 22px; overflow: hidden;
    box-shadow: 0 18px 40px rgba(0,0,0,.55);
  }
  .card-back {
    left: 120px; top: 100px; background: var(--card-black);
    display: flex; align-items: center; justify-content: center;
  }
  .back-wordmark {
    color: var(--card-white); font-weight: 800; font-size: 44px; letter-spacing: 2px;
  }
  .card-front { left: 520px; top: 480px; background: var(--card-white); }
  .corner-band { position: absolute; inset: 0; }
  .brand { position: absolute; left: 34px; top: 92px; }
  .brand-name {
    font-weight: 800; font-size: 46px; line-height: 1; color: var(--ink); letter-spacing: 1px;
  }
  .brand-sub {
    margin-top: 6px; font-weight: 600; font-size: 11px; letter-spacing: 6.3px; color: var(--ink);
  }
  .contact { position: absolute; left: 34px; top: 190px; }
  .person-name { color: var(--accent-red); font-weight: 800; font-size: 22px; line-height: 1.1; }
  .person-title { color: var(--muted); font-size: 13px; margin-bottom: 12px; }
  .contact-line {
    display: flex; align-items: center; gap: 10px;
    font-size: 13.5px; color: var(--ink); line-height: 1.6;
  }
  .contact-line svg { width: 12px; height: 12px; flex: none; }
</style>
</head>
<body>
<main class="stage">
  <section class="card card-back" aria-label="Card back">
    <span class="back-wordmark">CORVALT</span>
  </section>

  <section class="card card-front" aria-label="Card front">
    <svg class="corner-band" viewBox="0 0 560 320" aria-hidden="true">
      <path d="M300 0 H560 V250 C520 170 440 90 300 0 Z" fill="var(--card-black)"/>
      <path d="M0 250 L26 262 L0 280 Z" fill="var(--card-black)"/>
    </svg>

    <div class="brand">
      <div class="brand-name">CORVALT</div>
      <div class="brand-sub">CORVALT NZ LIMITED</div>
    </div>

    <div class="contact">
      <div class="person-name">MARK PELL</div>
      <div class="person-title">Managing Director</div>
      <div class="contact-line">
        <svg viewBox="0 0 24 24" aria-hidden="true"><path fill="var(--accent-red)" d="M6.6 10.8a15.1 15.1 0 0 0 6.6 6.6l2.2-2.2c.3-.3.7-.4 1-.2 1.1.4 2.3.6 3.6.6.6 0 1 .4 1 1V20c0 .6-.4 1-1 1C10.6 21 3 13.4 3 4c0-.6.4-1 1-1h3.5c.6 0 1 .4 1 1 0 1.3.2 2.5.6 3.6.1.3 0 .7-.2 1z"/></svg>
        <span>+64 027 604 91352</span>
      </div>
      <div class="contact-line">
        <svg viewBox="0 0 24 24" aria-hidden="true"><rect x="2" y="5" width="20" height="14" rx="1.5" fill="none" stroke="var(--accent-red)" stroke-width="2.2"/><path d="M3 6l9 7 9-7" fill="none" stroke="var(--accent-red)" stroke-width="2.2"/></svg>
        <span>mark.pell@corvalt-example.co.nz</span>
      </div>
    </div>
  </section>
</main>
</body>
</html>
```